We Buy Houses Postcard Design

Harborline Estate Partners is one of Baltimore‘s top real estate investing groups because we treat buyers and sellers like real people; not like numbers on a spreadsheet. We specialize in buying distressed properties including multi-family, commercial, retail, single family, and bank REO’s from sellers who need to sell fast. Our website is www.fernwickhomebuyers.example. Our phone number is (443) 517-2940. Both need to be on the card. Front and back sides are to be printed. Front full color, back black and white. We want our logo on the design somewhere. The logo can be found on the website. If you need the original files ask me for them. See attached as examples. Return address should be 487 W Garnet Ave, Suite 318, Baltimore, MD 21201. My name is Gregory. Address label is 1" x 2-5/8". Please leave room for it and postage on the back side.

Industry/Entity Type

Real Estate

```html
<!DOCTYPE html>
<html lang="en">
<head>
<meta charset="utf-8">
<title>We Buy Houses Postcard – Harborline Estate Partners</title>
<link href="https://fonts.googleapis.com/css2?family=Oswald:wght@500;600;700&family=Carlito:wght@400;700&display=swap" rel="stylesheet">
<style>
  :root {
    --canvas: #ffffff;
    --brand-red: #a01206;
    --headline-yellow: #f7e600;
    --offer-gold: #f3c21a;
    --offer-outline: #7a0c05;
    --white: #ffffff;
    --ink: #111111;
    --ink-soft: #333333;
    --dash: #555555;
    --sky-top: #4d86d6;
    --sky-mid: #bcd3ee;
    --lawn: #6fa43a;
    --lawn-dark: #3f7a22;
  }
  * { box-sizing: border-box; margin: 0; padding: 0; }
  html, body {
    width: 852px; height: 1200px; overflow: hidden;
    background: var(--canvas);
  }
  .canvas { position: relative; width: 852px; height: 1200px; }

  .postcard {
    position: absolute;
    left: 30px;
    width: 764px;
    box-shadow: 4px 8px 14px rgba(0,0,0,0.35);
    overflow: hidden;
  }
  .postcard--front { top: 28px; height: 556px; }
  .postcard--back  { top: 597px; height: 551px; background: var(--white); }

  /* Front */
  .front-photo {
    position: absolute; inset: 0;
    background:
      linear-gradient(180deg, var(--sky-top) 0%, var(--sky-mid) 40%, #d9d4c8 55%, var(--lawn) 72%, var(--lawn-dark) 100%);
  }
  .front-panel { position: absolute; inset: 0; }
  .front-copy {
    position: absolute; left: 0; top: 0; width: 302px;
    text-align: center;
    font-family: "Oswald", "Arial Narrow", sans-serif;
    font-weight: 700;
    line-height: 1;
    text-transform: uppercase;
  }
  .front-copy p { position: absolute; left: 0; width: 100%; white-space: nowrap; }
  .headline { color: var(--headline-yellow); font-size: 38px; letter-spacing: -0.5px; }
  .cta { color: var(--white); font-size: 50px; letter-spacing: -0.5px; }
  .cta--phone { font-size: 44px; letter-spacing: -1px; }
  .benefit { color: var(--headline-yellow); font-size: 39px; }
  .benefit--small { font-size: 32px; }

  .offer-line {
    position: absolute; left: 299px; width: 450px;
    font-family: "Oswald", "Arial Narrow", sans-serif;
    font-weight: 600; font-size: 33px; line-height: 1;
    text-transform: uppercase; white-space: nowrap;
    color: var(--offer-gold);
    text-shadow: 1px 1px 0 var(--offer-outline), -1px -1px 0 var(--offer-outline),
                 1px -1px 0 var(--offer-outline), -1px 1px 0 var(--offer-outline);
  }

  /* Back – black and white */
  .message {
    position: absolute; left: 33px; top: 57px; width: 362px;
    font-family: "Carlito", Calibri, sans-serif;
    font-size: 17px; line-height: 24px; color: var(--ink);
  }
  .message strong { font-variant: small-caps; font-weight: 700; letter-spacing: 0.2px; }
  .offer-list { list-style: none; margin: 10px 0 22px; }
  .offer-list li { position: relative; padding-left: 27px; }
  .offer-list li::before {
    content: ""; position: absolute; left: 3px; top: 10px;
    width: 6px; height: 6px; border-radius: 50%; background: var(--ink);
  }
  .divider {
    position: absolute; left: 417px; top: 41px; height: 467px;
    border-left: 2px dashed var(--dash);
  }
  .brand {
    position: absolute; left: 33px; top: 338px; width: 362px;
    display: flex; align-items: center; justify-content: center; gap: 10px;
    font-family: "Carlito", Calibri, sans-serif;
    font-size: 26px; font-weight: 700; color: var(--ink);
    white-space: nowrap;
  }
  .brand-mark { width: 16px; height: 16px; border-radius: 50%; background: var(--ink); flex: none; }
  .return-address {
    position: absolute; left: 33px; top: 380px; width: 362px; text-align: center;
    font-family: "Carlito", Calibri, sans-serif;
    font-size: 15px; line-height: 20px; color: var(--ink-soft);
  }
  .contact {
    position: absolute; left: 33px; width: 362px; text-align: center;
    font-family: "Oswald", "Arial Narrow", sans-serif;
    font-weight: 700; color: var(--ink); line-height: 1; white-space: nowrap;
  }
  .contact--web { top: 450px; font-size: 19px; letter-spacing: -0.3px; }
  .contact--phone { top: 478px; font-size: 32px; }
</style>
</head>
<body>
<main class="canvas">

  <section class="postcard postcard--front" aria-label="Postcard front">
    <div class="front-photo" role="img" aria-label="Photo of a hand holding house keys in front of a sold sign on a lawn, with another hand offering stacks of cash"></div>
    <svg class="front-panel" width="764" height="556" viewBox="0 0 764 556" aria-hidden="true">
      <polygon points="0,0 325,0 265,556 0,556" fill="var(--brand-red)"/>
    </svg>

    <div class="front-copy">
      <p class="headline" style="top:24px">We Buy Houses</p>
      <p class="headline" style="top:72px">In Baltimore,</p>
      <p class="headline" style="top:119px">Maryland</p>
      <p class="cta" style="top:186px">Fast Cash</p>
      <p class="cta" style="top:251px">Call Now</p>
      <p class="cta cta--phone" style="top:320px">443-517-2940</p>
      <p class="benefit" style="top:399px; left:-8px">Sell As Is</p>
      <p class="benefit" style="top:449px; left:-8px">No Costs</p>
      <p class="benefit benefit--small" style="top:497px; left:-8px">No Commissions</p>
    </div>

    <p class="offer-line" style="top:450px">Let us make a fair all-cash</p>
    <p class="offer-line" style="top:494px">offer on your house today!</p>
  </section>

  <section class="postcard postcard--back" aria-label="Postcard back">
    <div class="message">
      <p>My name is Gregory. <strong>I’m interested in buying your house.</strong> I offer:</p>
      <ul class="offer-list">
        <li>Cash for your house as-is</li>
        <li>No inspections or contingencies</li>
        <li>Fast and flexible closing</li>
        <li>No need to fix or clean out your home</li>
      </ul>
      <p>If you’re interested, please call me. There are no obligations and the worst case scenario is spending a few minutes on the phone!</p>
    </div>

    <div class="brand"><span class="brand-mark"></span>Harborline Estate Partners</div>
    <p class="return-address">487 W Garnet Ave, Suite 318<br>Baltimore, MD 21201</p>
    <p class="contact contact--web">www.fernwickhomebuyers.example</p>
    <p class="contact contact--phone">443-517-2940</p>

    <div class="divider" aria-hidden="true"></div>
  </section>

</main>
</body>
</html>
```